New look and feel for investment website

Hi

Our website needs a crisp and professional look and feel applying to it. Here’s the address: http://www.brightplinth.co.uk. Since posting the brief yesterday (Tuesday, 16 August), we've reduced the amount of content on the home page, which should make life a little easier for you. We will come back later today, with some points of reference in terms of sites we like the look of. (See below)

17 August, 1.20pm GMT. OK, comments generally on the designs submitted so far. Please keep in mind that images of graphs, piles of coins, paper money and pretty females are not what is required. Better to think in terms of abstract imagery instead. Ratios? Circles? Relationships? Patterns? Not money,sex,graphs etc. Hope that helps.

For guidance on look and feel, please refer to these sites, which we like:

http://www.morvelle.co.uk/
http://www.qz.com/
https://www.harrowfieldtamsin.com
https://www.pirelconcerns.com
https://www.kvantule.com
Updates

Here's the Tall Beacons logo created in AI CS5.

Our market is professional financial advisers and relatively sophisticated private investors. The look and feel therefore should be slick and sophisticated - not 'lively' and lightweight, more like a banking site. Please read the brief again where we've added a list of websites that we really like the look of to get a better feel for what we're looking for. Thanks once again, we appreciate the work you're putting in.

It's essential that all the elements that are on the current home page be included on all new designs. 

We use a device in our e-mails which you may wish to incorporate in your design.

Target Market(s)

Professional financial advisers. People who know about investment and money.

Industry/Entity Type

Investment

Requirements
Should not have
• Graphs or people.

```html
<!DOCTYPE html>
<html lang="en">
<head>
<meta charset="utf-8">
<title>Tall Beacons</title>
<link href="https://fonts.googleapis.com/css2?family=Arimo:wght@400;700&display=swap" rel="stylesheet">
<style>
:root{
  --bg-light:#dfe3e4;
  --bg-dark:#a9b3b5;
  --ink:#222;
  --ink-soft:#555;
  --ink-muted:#666;
  --nav-top:#3a3a3a;
  --nav-bottom:#161616;
  --white:#fff;
  --hero-bg:#0d0203;
  --hero-red:#b3121c;
  --orange:#e8921c;
  --gold-top:#f7c93a;
  --gold-bottom:#d99a06;
  --panel:#e4e7e8;
  --rule:#9aa1a3;
  --btn-top:#6a6a6a;
  --btn-bottom:#2c2c2c;
}
*{margin:0;padding:0;box-sizing:border-box}
html,body{width:1200px;height:731px;overflow:hidden}
body{
  position:relative;
  font-family:"Arimo",Arial,sans-serif;
  color:var(--ink);
  background:radial-gradient(ellipse at 55% 40%,var(--bg-light) 0%,#cdd3d5 55%,var(--bg-dark) 100%);
}
.abs{position:absolute}

.contact-bar{left:726px;top:0;width:334px;height:26px;background:rgba(235,238,239,.85);border-radius:0 0 5px 5px;display:flex;align-items:center;font-size:12px;color:#333}
.contact-bar .item{display:flex;align-items:center;gap:6px;padding:0 12px}
.contact-bar .item+.item{border-left:1px solid #999}

.brand{left:140px;top:28px;display:flex;align-items:center;gap:10px;font-size:46px;font-weight:400;color:#2a2a2a;letter-spacing:-1px;line-height:1}
.brand .dot{width:10px;height:10px;border-radius:50%;background:var(--orange)}

.search{left:843px;top:62px;display:flex}
.search .field{width:140px;height:21px;background:var(--white);border:1px solid #aab}
.search .btn{width:60px;height:21px;border:1px solid #aab;background:linear-gradient(#fafafa,#dcdfe3);font-size:11px;font-weight:700;color:#1d3466;display:flex;align-items:center;justify-content:center}

.nav{left:141px;top:88px;width:919px;height:40px;background:linear-gradient(var(--nav-top),var(--nav-bottom));border-radius:8px 8px 0 0;color:var(--white);font-size:12px;font-weight:700}
.nav .home-icon{left:20px;top:11px}
.nav .tab{position:absolute;top:12px}
.nav .tab.active{left:61px;top:7px;width:103px;height:33px;background:var(--white);color:var(--ink);border-radius:3px 3px 0 0;text-align:center;padding-top:7px}
.nav .sep{position:absolute;top:13px;width:1px;height:10px;background:var(--white)}
.nav .follow{position:absolute;left:792px;top:12px;font-weight:400}
.nav .social{position:absolute;top:9px;width:20px;height:20px;border-radius:3px}

.hero{left:141px;top:128px;width:919px;height:292px;background:var(--hero-bg);overflow:hidden}
.hero .visual{position:absolute;right:0;top:0;width:530px;height:292px;background:linear-gradient(100deg,var(--hero-bg) 0%,#3a0508 35%,var(--hero-red) 75%,#e23a40 100%)}
.hero h1{position:absolute;left:31px;top:50px;font-size:27px;font-weight:700;color:#e8e8e8;letter-spacing:-.5px}
.hero p{position:absolute;left:29px;top:88px;width:340px;font-size:15.5px;line-height:19.5px;color:var(--orange)}
.learn-more{left:29px;top:189px}

.lower{left:141px;top:420px;width:919px;height:254px;background:linear-gradient(var(--panel),#d9dddf)}
.col{position:absolute;top:0;height:254px}
.col+.col{border-left:1px solid var(--rule)}
.thumb{position:absolute;left:10px;top:15px;width:194px;height:93px;border:1px solid #c8cccd;background:var(--white);padding:4px}
.thumb div{width:100%;height:100%}
.col h2{position:absolute;left:13px;top:127px;font-size:17px;font-weight:700;color:var(--ink-soft)}
.col p{position:absolute;left:14px;top:150px;width:190px;font-size:11.4px;line-height:13.4px;color:var(--ink)}
.view-more{position:absolute;left:11px;top:204px;width:106px;height:24px}

.news{position:absolute;left:654px;top:0;width:265px;height:254px;border-left:1px solid var(--rule)}
.news .title{position:absolute;left:9px;top:13px;display:flex;align-items:flex-end;font-size:14px;font-weight:700;width:255px}
.news .title .slash{font-size:22px;font-style:italic;font-weight:700;margin-right:4px;line-height:18px}
.news .title .line{flex:1;border-bottom:1px solid #333;margin-left:4px;margin-bottom:3px}
.news .entry{position:absolute;left:11px;width:235px;font-size:11.4px;line-height:13.8px;color:var(--ink-muted)}
.news .entry b{color:var(--ink-soft)}
.news .entry .more{color:var(--ink);margin-left:10px}
.scroll{position:absolute;left:252px;top:44px;width:5px;height:200px;background:#333;border-radius:3px}
.scroll .thumb-s{position:absolute;left:-2px;top:2px;width:9px;height:14px;background:var(--white);border:1px solid #888;border-radius:3px}

.footer{left:139px;top:688px;width:921px;border-top:1px solid #777;padding-top:7px;font-size:10px;color:#333;display:flex;justify-content:space-between}
.footer nav span+span::before{content:"I";margin:0 8px;color:#555}
</style>
</head>
<body>

<div class="abs contact-bar">
  <div class="item">
    <svg width="18" height="14" viewBox="0 0 18 14"><path d="M3 2c2-2 4 0 3 2L5 5c1 2 3 4 5 5l1-1c2-1 4 1 2 3-2 2-6 1-9-3S1 4 3 2z" fill="#333"/></svg>
    (+44) 01632.960.418
  </div>
  <div class="item">
    <svg width="17" height="13" viewBox="0 0 17 13"><rect x="1" y="2" width="15" height="10" fill="none" stroke="#333" stroke-width="1.6"/><path d="M1 2l7.5 6L16 2" fill="none" stroke="#333" stroke-width="1.6"/></svg>
    marketing@tallbeacons.co.uk
  </div>
</div>

<div class="abs brand">Tall Beacons<span class="dot"></span></div>

<div class="abs search"><div class="field"></div><div class="btn">Search</div></div>

<nav class="abs nav">
  <svg class="abs home-icon" width="22" height="18" viewBox="0 0 22 18"><path d="M11 1L1 9h3v8h5v-5h4v5h5V9h3z" fill="#cfcfcf"/></svg>
  <span class="tab active">Home</span>
  <span class="tab" style="left:198px">About us</span>
  <span class="sep" style="left:283px"></span>
  <span class="tab" style="left:317px">Company</span>
  <span class="sep" style="left:405px"></span>
  <span class="tab" style="left:436px">Services</span>
  <span class="sep" style="left:515px"></span>
  <span class="tab" style="left:556px">Contact us</span>
  <span class="follow">Follow us in</span>
  <span class="social" style="left:861px;background:#3fb4dd"></span>
  <span class="social" style="left:886px;background:#3b64ad"></span>
</nav>

<section class="abs hero">
  <div class="visual" role="img" aria-label="Abstract red digital blocks receding into depth"></div>
  <h1>Welcome to our site.</h1>
  <p>Lorem ipsum dolor sit amet, consectetuer adipiscing elit, sed diam nonummy nibh euismod tincidunt ut laoreet dolore magna aliquam erat volutpat. Ut wisi enim ad minim</p>
  <svg class="abs learn-more" width="143" height="38" viewBox="0 0 143 38">
    <defs><linearGradient id="gold" x1="0" y1="0" x2="0" y2="1"><stop offset="0" stop-color="#f7c93a"/><stop offset="1" stop-color="#d99a06"/></linearGradient></defs>
    <path d="M3 0h125l14 19-14 19H3a3 3 0 0 1-3-3V3a3 3 0 0 1 3-3z" fill="url(#gold)"/>
    <text x="66" y="24" text-anchor="middle" font-family="Arimo, Arial, sans-serif" font-size="13" font-weight="700" fill="#fff">LEARN MORE</text>
  </svg>
</section>

<section class="abs lower">
  <div class="col" style="left:0;width:216px">
    <div class="thumb"><div role="img" aria-label="Business strategy photograph" style="background:linear-gradient(90deg,#e6e9ec,#bfc6cc 60%,#3b4452)"></div></div>
    <h2>Services</h2>
    <p>Lorem Ipsum is simply dummy text of the printing and typesetting industry. text ever since the 1500s,</p>
    <svg class="view-more" viewBox="0 0 106 24"><defs><linearGradient id="dg" x1="0" y1="0" x2="0" y2="1"><stop offset="0" stop-color="#6a6a6a"/><stop offset="1" stop-color="#2c2c2c"/></linearGradient></defs><rect width="106" height="24" rx="3" fill="url(#dg)"/><rect x="88" y="1" width="17" height="22" rx="2" fill="#555"/><path d="M94 9l2.5 2.5L99 9M94 13l2.5 2.5L99 13" stroke="#fff" fill="none" stroke-width="1.2"/><text x="42" y="16" text-anchor="middle" font-family="Arimo, Arial, sans-serif" font-size="11.5" font-weight="700" fill="#fff">VIEW MORE</text></svg>
  </div>
  <div class="col" style="left:216px;width:221px">
    <div class="thumb"><div role="img" aria-label="Documents and pens on a desk" style="background:linear-gradient(135deg,#f1f3f5,#c9d2dc 50%,#8aa0b8)"></div></div>
    <h2>About us</h2>
    <p>Lorem Ipsum is simply dummy text of the printing and typesetting industry. text ever since the 1500s,</p>
    <svg class="view-more" viewBox="0 0 106 24"><rect width="106" height="24" rx="3" fill="url(#dg)"/><rect x="88" y="1" width="17" height="22" rx="2" fill="#555"/><path d="M94 9l2.5 2.5L99 9M94 13l2.5 2.5L99 13" stroke="#fff" fill="none" stroke-width="1.2"/><text x="42" y="16" text-anchor="middle" font-family="Arimo, Arial, sans-serif" font-size="11.5" font-weight="700" fill="#fff">VIEW MORE</text></svg>
  </div>
  <div class="col" style="left:437px;width:217px">
    <div class="thumb"><div role="img" aria-label="Glass office towers against a blue sky" style="background:linear-gradient(160deg,#1f4f8f,#6f9fd6 45%,#dfe9f5 55%,#2a5a99)"></div></div>
    <h2>Our Company</h2>
    <p>Lorem Ipsum is simply dummy text of the printing and typesetting industry. text ever since the 1500s,</p>
    <svg class="view-more" viewBox="0 0 106 24"><rect width="106" height="24" rx="3" fill="url(#dg)"/><rect x="88" y="1" width="17" height="22" rx="2" fill="#555"/><path d="M94 9l2.5 2.5L99 9M94 13l2.5 2.5L99 13" stroke="#fff" fill="none" stroke-width="1.2"/><text x="42" y="16" text-anchor="middle" font-family="Arimo, Arial, sans-serif" font-size="11.5" font-weight="700" fill="#fff">VIEW MORE</text></svg>
  </div>
  <aside class="news">
    <div class="title"><span class="slash">/</span>News Update<span class="line"></span></div>
    <div class="entry" style="top:51px"><b>Lorem Ipsum</b> (August 2011)<br>Lorem Ipsum is simply dummy text of the printing and typesetting industry. text ever since the 1500s......<span class="more">Read more</span></div>
    <div class="entry" style="top:120px"><b>Lorem Ipsum</b> (August 2011)<br>Lorem Ipsum is simply dummy text of the printing and typesetting industry. text ever since the 1500s......<span class="more">Read more</span></div>
    <div class="entry" style="top:190px"><b>Lorem Ipsum</b> (August 2011)<br>Lorem Ipsum is simply dummy text of the printing and typesetting industry. text ever since the 1500s......<span class="more">Read more</span></div>
    <div class="scroll"><div class="thumb-s"></div></div>
  </aside>
</section>

<footer class="abs footer">
  <span>© tallbeacons 2011, All rights reserved</span>
  <nav><span>Home</span><span>About us</span><span>Company</span><span>Services</span><span>Contact us</span></nav>
</footer>

</body>
</html>
```